Orbell Consulting- executive coaching business

looking for business card design for a newly started coaching business.
specialising in Exective coaching, Leadership, NLP and Motivation.
Looking for a simple, classy design using the existing logo attached and colour themes that complement the logo.
No red or orange in the business card design please.

Target Market(s)

Defence and Veteran community

Industry/Entity Type

Life Coaching

Contact Information for Business Card

looking for business cards for newly started coaching business.
specialising in Exective Coaching, Leadership, NLP and Motivation

Font styles to use
Serif
Script

Colors
0556a4
3176b5
86cfc6
33b8a4

Requirements
Must have
• Logo
• Email address- Jess@orbellconsulting.com.au
• Contact number
• Services provided - Executive Coaching, Leadership, NLP and Motivational Mapping.
Nice to have
• Same colours as logo
Should not have
• Red or orange

```html
<!DOCTYPE html>
<html lang="en">
<head>
<meta charset="utf-8">
<title>Orbell Consulting – Business Cards</title>
<link rel="stylesheet" href="https://fonts.googleapis.com/css2?family=Raleway:wght@400;500;600;700&display=swap">
<style>
  :root {
    --brand-blue: #1b74bb;
    --brand-blue-dark: #0556a4;
    --card-white: #ffffff;
    --stage: #e9ebee;
    --shadow: rgba(20, 30, 45, 0.18);
  }
  * { box-sizing: border-box; margin: 0; padding: 0; }
  html, body { width: 1200px; height: 960px; overflow: hidden; }
  body {
    background: var(--stage);
    font-family: "Raleway", sans-serif;
    position: relative;
  }
  .card {
    position: absolute;
    width: 560px;
    height: 320px;
    background: var(--card-white);
    border-radius: 12px;
    box-shadow: 0 10px 30px var(--shadow);
    overflow: hidden;
  }

  /* ---------- back of card ---------- */
  .card-back { left: 80px; top: 110px; }
  .card-back .brand {
    position: absolute;
    left: 24px; top: 64px;
    width: 220px;
    display: flex; align-items: center; gap: 8px;
    white-space: nowrap;
  }
  .brand-dot {
    width: 20px; height: 20px;
    border-radius: 50%;
    background: var(--brand-blue);
    flex: none;
  }
  .brand-name {
    font-weight: 700;
    color: var(--brand-blue);
    letter-spacing: 0.3px;
    text-transform: uppercase;
  }
  .card-back .brand-name { font-size: 14px; }

  .contact-panel {
    position: absolute;
    right: 0; top: 0;
    width: 300px; height: 146px;
    background: var(--brand-blue);
    padding: 42px 0 0 28px;
    color: var(--card-white);
  }
  .contact-line {
    display: flex; align-items: center; gap: 12px;
    font-size: 15px;
    margin-bottom: 14px;
    white-space: nowrap;
  }
  .contact-icon {
    width: 20px; height: 20px;
    border-radius: 50%;
    background: var(--card-white);
    display: flex; align-items: center; justify-content: center;
    flex: none;
  }
  .contact-icon svg { width: 12px; height: 12px; }

  .services {
    position: absolute;
    right: 0; top: 154px;
    width: 330px;
  }
  .services-title {
    font-size: 22px;
    font-weight: 500;
    color: var(--brand-blue);
    letter-spacing: 0.5px;
    padding-left: 24px;
    margin-bottom: 6px;
    white-space: nowrap;
  }
  .service-bar {
    background: var(--brand-blue);
    color: var(--card-white);
    font-size: 15px;
    height: 24px;
    line-height: 24px;
    padding-left: 22px;
    margin-bottom: 5px;
    margin-left: auto;
    white-space: nowrap;
  }
  .service-bar:nth-child(2) { width: 310px; }
  .service-bar:nth-child(3) { width: 290px; }
  .service-bar:nth-child(4) { width: 270px; }
  .service-bar:nth-child(5) { width: 250px; }

  /* ---------- front of card ---------- */
  .card-front { left: 560px; top: 530px; }
  .card-front .brand {
    position: absolute;
    inset: 0;
    display: flex; flex-direction: column;
    align-items: center; justify-content: center;
    gap: 18px;
  }
  .card-front .brand-dot { width: 70px; height: 70px; }
  .card-front .brand-name { font-size: 36px; }
</style>
</head>
<body>

  <section class="card card-back" aria-label="Business card back">
    <div class="brand">
      <span class="brand-dot"></span>
      <span class="brand-name">Orbell Consulting</span>
    </div>

    <div class="contact-panel">
      <div class="contact-line">
        <span class="contact-icon">
          <svg viewBox="0 0 24 24"><rect x="3" y="6" width="18" height="12" rx="1.5" fill="#1b74bb"/><path d="M3.5 7l8.5 6 8.5-6" fill="none" stroke="#fff" stroke-width="1.6"/></svg>
        </span>
        <span>Jess@orbellconsulting.com.au</span>
      </div>
      <div class="contact-line">
        <span class="contact-icon">
          <svg viewBox="0 0 24 24"><path fill="#1b74bb" d="M6.6 10.8a15 15 0 0 0 6.6 6.6l2.2-2.2a1 1 0 0 1 1-.25 11.4 11.4 0 0 0 3.6.57 1 1 0 0 1 1 1V20a1 1 0 0 1-1 1A17 17 0 0 1 3 4a1 1 0 0 1 1-1h3.5a1 1 0 0 1 1 1c0 1.25.2 2.45.57 3.6a1 1 0 0 1-.25 1z"/></svg>
        </span>
        <span>+61 400 218 574</span>
      </div>
    </div>

    <div class="services">
      <h2 class="services-title">SERVICES PROVIDED</h2>
      <div class="service-bar">Executive Coaching</div>
      <div class="service-bar">Leadership</div>
      <div class="service-bar">NLP</div>
      <div class="service-bar">Motivational Mapping</div>
    </div>
  </section>

  <section class="card card-front" aria-label="Business card front">
    <div class="brand">
      <span class="brand-dot"></span>
      <span class="brand-name">Orbell Consulting</span>
    </div>
  </section>

</body>
</html>
```